Italian Dinning Table and wardrobe Selling Website

We need a website design for a reputable furniture company deals in the manufacture of Italian dinning tables and wardrobe. We provide our services to USA based customers.

The categories of the website are
- Home page
- Product page
- The page where all the items are sold
- The shopping cart page

The website is required to have several areas of products with prices that can be added to shopping cart.
Also the website should have customer login facility along with privacy policy, contact us, about us and terms of use
Preferred colors are brown, black and pink,

It Company

```html
<!DOCTYPE html>
<html lang="en">
<head>
<meta charset="utf-8">
<title>Casa Furniture</title>
<link href="https://fonts.googleapis.com/css2?family=Open+Sans:wght@400;600;700&family=Source+Sans+3:wght@300;400&display=swap" rel="stylesheet">
<style>
:root{
  --pink:#d81b7a;
  --pink-band:#d6237f;
  --magenta:#c3147a;
  --plum:#8b0b5a;
  --maroon:#7a0a3c;
  --footer:#1e0818;
  --charcoal:#343839;
  --ink:#2b2b2b;
  --muted:#6a6a6a;
  --line:#9a9a9a;
  --white:#ffffff;
  --paper:#f4f4f4;
  --badge:#4aa52e;
}
*{box-sizing:border-box;margin:0;padding:0}
html,body{width:1200px;height:3797px;overflow:hidden}
body{position:relative;background:var(--white);font-family:"Open Sans",Arial,sans-serif;color:var(--ink)}
.abs{position:absolute}

/* header */
.site-header{left:0;top:0;width:1200px;height:114px;background:var(--paper)}
.brand{left:70px;top:6px;font-family:"Source Sans 3",Arial,sans-serif;font-weight:300;font-size:100px;line-height:100px;color:var(--ink);letter-spacing:2px}
.login{right:78px;top:50px;display:flex;align-items:center;gap:16px;font-size:13px;color:var(--pink);font-weight:600}
.social-top{right:72px;top:86px;display:flex;gap:20px}
.social-top span{width:20px;height:20px;border-radius:50%;background:var(--ink)}

/* nav */
.main-nav{left:0;top:114px;width:1200px;height:38px;background:var(--pink);display:flex;justify-content:center;align-items:center;gap:30px}
.main-nav a{color:var(--white);text-decoration:none;font-size:13px;font-weight:600}
.main-nav a.current{color:#1a0010}

/* hero */
.hero{left:0;top:152px;width:1200px;height:798px;background:linear-gradient(135deg,#3e5a2a 0%,#8a7a58 30%,#d9b98c 55%,#e9d4b4 75%,#c9a77a 100%)}
.hero-arrow{top:520px}
.hero-dots{left:558px;top:875px;display:flex;gap:8px}
.hero-dots span{width:13px;height:13px;border-radius:50%;background:#333}
.hero-dots span.on{background:var(--pink)}

/* about */
.about-title{left:0;top:1060px;width:1200px;text-align:center;font-family:"Source Sans 3",Arial,sans-serif;font-size:52px;color:var(--maroon)}
.about-text{left:70px;top:1160px;width:1060px;text-align:center;font-size:13.5px;line-height:21px;color:#333}
.more{color:var(--pink);font-size:12px;text-decoration:none}
.about-more{left:0;top:1303px;width:1200px;text-align:center}

/* bands */
.band{left:0;width:1200px;height:61px;color:var(--white);text-align:center;font-family:"Source Sans 3",Arial,sans-serif;font-size:46px;line-height:61px}
.band-gallery{top:1413px;background:var(--pink-band)}
.band-shop{top:2172px;background:var(--magenta)}
.band-contact{top:2816px;background:var(--plum)}

/* gallery */
.gallery{left:73px;top:1504px;width:1056px;display:grid;grid-template-columns:repeat(4,243px);grid-auto-rows:280px;column-gap:28px;row-gap:20px}
.tile{border:1px solid #ddd}
.t1{background:linear-gradient(160deg,#d8d8d8,#5a4a3e)}
.t2{background:linear-gradient(160deg,#e6e0d8,#1e2e2e 60%,#c08848)}
.t3{background:linear-gradient(160deg,#f6ecd8,#c9a77a 55%,#3a2a22)}
.t4{background:linear-gradient(160deg,#c8d4de,#f2f2f2 55%,#b06a2a)}
.t5{background:linear-gradient(160deg,#cfcfcf,#f0f0f0 45%,#4a3226)}
.t6{background:linear-gradient(160deg,#3a2a24,#6a5040 50%,#1e1816)}
.t7{background:linear-gradient(160deg,#f4f4f4,#dcdcdc 55%,#7a6a5a)}
.t8{background:linear-gradient(160deg,#f0f0f0,#9ab4c8 55%,#c8782a)}
.scroll-track{left:1152px;top:1504px;width:28px;height:580px;background:#ececec}
.scroll-thumb{left:1154px;top:1554px;width:24px;height:62px;background:#b5b5b5}

/* shopping */
.shop{left:0;top:2233px;width:1200px;height:504px;background:var(--charcoal)}
.cards{left:73px;top:2274px;display:flex;gap:12px}
.card{width:254px;height:438px;background:var(--white);position:relative}
.card-img{height:195px;background:linear-gradient(150deg,#f0ede6,#d9d2c4 50%,#8a8a8a)}
.card-img.c2{background:linear-gradient(150deg,#2a2a2a,#e8e8e8 45%,#9ab0c0)}
.card-img.c3{background:linear-gradient(150deg,#2e2e2e,#cfd9e0 50%,#7a8a6a)}
.card-img.c4{background:linear-gradient(150deg,#5a3a22,#e8e8e8 50%,#c8782a)}
.fee-row{display:flex;justify-content:space-between;align-items:center;padding:12px 12px 0 12px;font-size:11px;color:#222}
.badge{width:34px;height:14px;background:var(--badge)}
.card-title{text-align:center;margin-top:52px;font-size:17px;font-weight:700;color:#111}
.card-desc{text-align:center;margin:14px 16px 0;font-size:13px;line-height:21px;color:#222}
.card-more{position:absolute;left:0;bottom:10px;width:100%;text-align:center}
.shop-arrow{top:2470px}

/* contact */
.field{height:34px;border:1.5px solid var(--line);font-size:13px;color:#777;padding:7px 12px;background:var(--white)}
.f-first{left:73px;top:2929px;width:451px}
.f-last{left:585px;top:2929px;width:542px}
.f-phone{left:73px;top:2993px;width:451px}
.f-email{left:73px;top:3056px;width:451px}
.f-msg{left:585px;top:2993px;width:542px;height:96px}

/* footer */
.site-footer{left:0;top:3145px;width:1200px;height:223px;background:var(--footer)}
.social-foot{left:420px;top:3180px;display:flex;gap:29px}
.social-foot span{width:71px;height:71px;border-radius:50%;border:4px solid var(--white)}
.foot-nav{left:0;top:3292px;width:1200px;display:flex;justify-content:center;gap:30px}
.foot-nav a{color:var(--white);font-size:13px;font-weight:600;text-decoration:none}
.foot-nav a.current{color:var(--pink)}
.copyright{left:0;top:3334px;width:1200px;text-align:center;font-size:12px;color:#5a3a4a}

/* map */
.map{left:0;top:3368px;width:1200px;height:429px;background:linear-gradient(160deg,#cfc8bd,#bdb6ab 50%,#d6d0c4)}
</style>
</head>
<body>

<header class="abs site-header">
  <div class="abs brand">LOGO</div>
  <div class="abs login">
    <svg width="26" height="26" viewBox="0 0 26 26" aria-hidden="true"><circle cx="10" cy="10" r="7" fill="none" stroke="#d81b7a" stroke-width="3"/><line x1="15" y1="15" x2="23" y2="23" stroke="#d81b7a" stroke-width="4" stroke-linecap="round"/></svg>
    <span>LOGIN</span>
  </div>
  <div class="abs social-top" aria-label="Social links"><span></span><span></span><span></span><span></span></div>
</header>

<nav class="abs main-nav">
  <a class="current" href="#">HOME</a><a href="#">PRODUCT</a><a href="#">GALLERY</a><a href="#">SHOPPING</a><a href="#">CONTACT</a>
</nav>

<section class="abs hero" role="img" aria-label="Wicker dining chairs and table on a sunny terrace"></section>
<svg class="abs hero-arrow" style="left:14px" width="24" height="40" viewBox="0 0 24 40" aria-hidden="true"><polyline points="18,6 6,20 18,34" fill="none" stroke="#111" stroke-width="5"/></svg>
<svg class="abs hero-arrow" style="left:1162px" width="24" height="40" viewBox="0 0 24 40" aria-hidden="true"><polyline points="6,6 18,20 6,34" fill="none" stroke="#111" stroke-width="5"/></svg>
<div class="abs hero-dots"><span class="on"></span><span></span><span></span><span></span></div>

<h1 class="abs about-title">About Our Company</h1>
<p class="abs about-text">Lorem ipsum dolor sit amet conse ctetur adipisicing elit, sed do eiusmod tempor incididunt ut labore et dolore magna aliqua. Ut enim ad minim veniam, quis nostrud exercitation ullamco laboris nisi ut aliquip ex ea commodo consequat. Duis aute irure dolor in reprehenderit in voluptate velit esse cillum dolore eu fugiat nulla pariatur. Excepteur sint occaecat cupidatat non proident, sunt in culpa qui officia deserunt mollit anim id est laborum. Lorem ipsum dolor sit amet conse ctetur adipisicing elit, sed do eiusmod tempor incididunt ut labore et dolore magna aliqua. Ut enim ad minim veniam, quis nostrud exercitation ullamco laboris nisi ut aliquip ex ea commodo consequat. Duis aute irure dolor in reprehenderit in voluptate velit esse cillum dolore eu fugiat nulla pariatur.</p>
<div class="abs about-more"><a class="more" href="#">MORE INFO.</a></div>

<h2 class="abs band band-gallery">GALLERY</h2>
<div class="abs gallery">
  <div class="tile t1" role="img" aria-label="Modern kitchen with wood cabinets"></div>
  <div class="tile t2" role="img" aria-label="Leather dining chair"></div>
  <div class="tile t3" role="img" aria-label="Bright dining room with dark table"></div>
  <div class="tile t4" role="img" aria-label="White kitchen with wood ceiling"></div>
  <div class="tile t5" role="img" aria-label="Kitchen island with bar stools"></div>
  <div class="tile t6" role="img" aria-label="Dark wood dining set"></div>
  <div class="tile t7" role="img" aria-label="White tiled kitchen and dining area"></div>
  <div class="tile t8" role="img" aria-label="Glass dining table by windows"></div>
</div>
<div class="abs scroll-track"></div>
<div class="abs scroll-thumb"></div>

<h2 class="abs band band-shop">SHOPPING</h2>
<section class="abs shop"></section>
<svg class="abs shop-arrow" style="left:14px" width="22" height="34" viewBox="0 0 22 34" aria-hidden="true"><polyline points="16,5 6,17 16,29" fill="none" stroke="#fff" stroke-width="4"/></svg>
<svg class="abs shop-arrow" style="left:1162px" width="22" height="34" viewBox="0 0 22 34" aria-hidden="true"><polyline points="6,5 16,17 6,29" fill="none" stroke="#fff" stroke-width="4"/></svg>
<div class="abs cards">
  <article class="card"><div class="card-img" role="img" aria-label="Living room with white sofa"></div><div class="fee-row"><span>FEE: $299</span><span class="badge"></span></div><h3 class="card-title">Verona Set</h3><p class="card-desc">Automated management strategy that turns your losing trades into winners using a unique imbalanced hedging strategy.</p><a class="more card-more" href="#">MORE INFO.</a></article>
  <article class="card"><div class="card-img c2" role="img" aria-label="Open kitchen with pendant lights"></div><div class="fee-row"><span>FEE: $299</span><span class="badge"></span></div><h3 class="card-title">Verona Set</h3><p class="card-desc">Automated management strategy that turns your losing trades into winners using a unique imbalanced hedging strategy.</p><a class="more card-more" href="#">MORE INFO.</a></article>
  <article class="card"><div class="card-img c3" role="img" aria-label="Kitchen with garden view"></div><div class="fee-row"><span>FEE: $299</span><span class="badge"></span></div><h3 class="card-title">Verona Set</h3><p class="card-desc">Automated management strategy that turns your losing trades into winners using a unique imbalanced hedging strategy.</p><a class="more card-more" href="#">MORE INFO.</a></article>
  <article class="card"><div class="card-img c4" role="img" aria-label="White kitchen counter with wood ceiling"></div><div class="fee-row"><span>FEE: $299</span><span class="badge"></span></div><h3 class="card-title">Verona Set</h3><p class="card-desc">Automated management strategy that turns your losing trades into winners using a unique imbalanced hedging strategy.</p><a class="more card-more" href="#">MORE INFO.</a></article>
</div>

<h2 class="abs band band-contact">CONTACT US</h2>
<div class="abs field f-first">First Name</div>
<div class="abs field f-last">Last Name</div>
<div class="abs field f-phone">Phone</div>
<div class="abs field f-email">Email</div>
<div class="abs field f-msg">How can we help you</div>

<footer class="abs site-footer"></footer>
<div class="abs social-foot" aria-label="Social links"><span></span><span></span><span></span><span></span></div>
<nav class="abs foot-nav"><a class="current" href="#">HOME</a><a href="#">PRODUCT</a><a href="#">GALLERY</a><a href="#">SHOPPING</a><a href="#">CONTACT</a></nav>
<p class="abs copyright">Casa © 2016, Privacy Policy</p>

<div class="abs map" role="img" aria-label="Street map showing store locations"></div>

</body>
</html>
```